Veridan Crest Business Cards

Veridan Crest Prestige Portfolio Group is a global representation business focusing on high end luxury. We need business cards to epitomize our global, luxury delivery model.

Target Market(s)

Global Representation in the hospitality industry

Industry/Entity Type

Hospitality

Contact Information for Business Card

name
title
email: first.last@vc-ppg.com
web: www.vc-ppg.com
mobile:

Requirements
Must have
• double sided design
• incorporate logo colours
• have logo prominent
Should not have
• no designs not incorporating logo colours.

```html
<!DOCTYPE html>
<html lang="en">
<head>
<meta charset="utf-8">
<title>Veridan Crest Business Cards</title>
<link href="https://fonts.googleapis.com/css2?family=Cinzel:wght@400;600&family=Marcellus&display=swap" rel="stylesheet">
<style>
  :root {
    --backdrop: #2b2d31;
    --card: #1d1d1f;
    --gold: #b79a5c;
    --gold-light: #d8c79c;
    --ivory: #dedbd3;
    --muted: #c9c6bf;
  }
  * { margin: 0; padding: 0; box-sizing: border-box; }
  html, body {
    width: 1200px; height: 900px; overflow: hidden;
    background: var(--backdrop);
  }
  .stage {
    width: 1200px; height: 900px;
    display: flex; align-items: center; justify-content: center; gap: 40px;
  }
  .card {
    width: 540px; height: 310px;
    background: var(--card);
    border-radius: 24px;
    position: relative;
    box-shadow: 0 14px 30px rgba(0,0,0,.35);
  }
  .brand {
    display: flex; flex-direction: column; align-items: center;
    font-family: "Cinzel", serif; font-weight: 600; color: var(--gold);
    text-align: center;
  }
  .brand-mark {
    width: 14px; height: 14px; border-radius: 50%;
    background: var(--gold); margin-bottom: 14px;
  }
  .brand-name { font-size: 40px; letter-spacing: 2px; line-height: 1; }
  .brand-sub { font-size: 13px; letter-spacing: 3px; margin-top: 10px; }

  /* contact side */
  .card-contact .brand {
    position: absolute; left: 34px; top: 92px; width: 230px;
  }
  .card-contact .brand-name { font-size: 32px; }
  .card-contact .brand-sub { font-size: 10px; letter-spacing: 2px; }
  .person {
    position: absolute; left: 290px; top: 84px;
  }
  .person-name {
    font-family: "Cinzel", serif; font-weight: 400;
    font-size: 27px; letter-spacing: 2px; color: var(--ivory);
  }
  .person-title {
    font-family: "Cinzel", serif; font-size: 13px; letter-spacing: 2px;
    color: var(--gold); margin-top: 4px;
  }
  .contact-list { list-style: none; margin-top: 24px; }
  .contact-list li {
    display: flex; align-items: center; gap: 10px;
    font-family: "Marcellus", serif; font-size: 15px; color: var(--muted);
    margin-bottom: 9px;
  }
  .contact-list svg { width: 14px; height: 14px; flex: none; }

  /* logo side */
  .card-logo .brand {
    position: absolute; left: 0; right: 0; top: 90px;
  }
  .card-logo .brand-name { color: var(--gold-light); }
  .site {
    position: absolute; left: 0; right: 0; bottom: 70px;
    text-align: center; font-family: "Marcellus", serif;
    font-size: 14px; letter-spacing: 4px; color: var(--ivory);
  }
</style>
</head>
<body>
<main class="stage">
  <section class="card card-contact">
    <div class="brand">
      <span class="brand-mark"></span>
      <span class="brand-name">Veridan Crest</span>
      <span class="brand-sub">PRESTIGE PORTFOLIO GROUP</span>
    </div>
    <div class="person">
      <p class="person-name">YOUR NAME</p>
      <p class="person-title">JOB TITLE</p>
      <ul class="contact-list">
        <li>
          <svg viewBox="0 0 14 14"><rect x="3.5" y="1" width="7" height="12" rx="1.2" fill="none" stroke="#b79a5c" stroke-width="1.3"/><circle cx="7" cy="11" r=".8" fill="#b79a5c"/></svg>
          000 000 0000
        </li>
        <li>
          <svg viewBox="0 0 14 14"><rect x="1" y="3" width="12" height="8.5" rx="1" fill="#b79a5c"/><path d="M1.5 3.5 7 8l5.5-4.5" fill="none" stroke="#1d1d1f" stroke-width="1.1"/></svg>
          first.last@vc-ppg.com
        </li>
        <li>
          <svg viewBox="0 0 14 14"><circle cx="7" cy="7" r="5.8" fill="none" stroke="#b79a5c" stroke-width="1.2"/><ellipse cx="7" cy="7" rx="2.5" ry="5.8" fill="none" stroke="#b79a5c" stroke-width="1"/><path d="M1.2 7h11.6" stroke="#b79a5c" stroke-width="1"/></svg>
          www.vc-ppg.com
        </li>
      </ul>
    </div>
  </section>

  <section class="card card-logo">
    <div class="brand">
      <span class="brand-mark"></span>
      <span class="brand-name">Veridan Crest</span>
      <span class="brand-sub">PRESTIGE PORTFOLIO GROUP</span>
    </div>
    <p class="site">WWW.VC-PPG.COM</p>
  </section>
</main>
</body>
</html>
```